Book Marketing Site for authors needs redesign

I need a site redesign for the site www.quorvanta.com I would like to have it designed/created in Wordpress so that I can change/edit the text as necessary. Ideally, we can simplify the site so that Wordpress updates do not impact the functionality of the site.

I want to continue to use the Quorvant logo, so I would like the site to work the existing logo. I am also planning to add the tag line Book Marketing Simplified so please incorporate the tag line with the logo and the site.

Initially, I would like to see the page design template and then once that is approved, you to program the site. Wherever, I have indicated that we would capture email addresses; I would like to set it up so that the names are captured in my Mellow Relay account.

Below are the elements that will need to be part of the site:
_______

Elements that should be above the fold:

• Chirply, Facemuro, Vexor+ and Pindle up buttons with the copy “Connect with Miriam”
o
• The copy “Sign up for our free newsletter and receive our list of Top Chirply Tips for Authors Free!” with a box to enter email address. The button should say “Go” not "Submit".
• A space/box for a short, 10-15 word testimonials. The testimonials will need to change from page to page.

Nav Bar/sub nav bars

Services
Packages Speaking Testimonials
FAQ
-
About Us
Speaking
-
Resources
-
Our clients
Testimonials
-
Blog
-
Contact Us

Home page
• Should have the following copy:
High Impact Book Marketing for Authors

QuorVant Marketing is book marketing service that that provides authors with an effective,
affordable approach to marketing their book.

We provide marketing coaching and consulting services that accelerate book sales, target your ideal reader and develop a community of fans that will promote your book for you.

Using high impact, low cost marketing strategies, we will develop a book marketing strategy that achieves your goals and accommodates your budget

Do you
• Want to be a best selling author, but need someone to show you the way

• Wonder what is the secret to achieving high book sales?

• Worry that you aren’t doing the right things to ensure that your book is a success?

• Need someone to help keep your spirits up and maintain momentum?

• Please put the following copy in a box at the bottom of the copy.
o Are you ready for results? Call now for a free consultation 318-546-0821

Services Page
• Copy to come

Packages Page

FAQ Page
• Same as existing site

About page
• Same as existing site

Speaking Page

Speaking

If you’re looking to create an exceptional program that your attendees won’t be able to stop talking about, you have found it!

Miriam Tolberg, a leader in book marketing, has ability to make sophisticated internet concepts easy and accessible, and the unique ability to not only to inform, but also to inspire. Her presentations leave participants with tangible, actionable ideas proven to increase book sales.

Miriam's talks combine practical step-by-step instructions, real-life examples with plenty of humor. Call 318-546-0821 to book her now!

Miriam’s most popular talks:

• Unlocking the Power of Pagewell
• How to Simplify Social Media
• The Ideal Author Website
• Orvex: What You Need to Know to Succeed

Resources page
• Same as existing site

Clients
• Same as existing site

Testimonials
• I would like to be able to put a image of book cover next to the testimonial on this page.

Blog page
• Please add the following elements:
• A way to sign up for the blog via RSS
o Each blog article should have a way to Facemuro like, Chirp, V+, Plink and Wanderclip the article

Contact us page
• Same as existing site

Site Map
• Please make sure to include a site map.

Chirply and Facemuro headers
• Please provide both with consistent branding.

Target Market(s)

Clients are both traditionally and indie published authors trying to be the next P.J. Harwick!

Industry/Entity Type

Marketing

Requirements
Must have
• Elements that should be above the fold:

o

```html
<!DOCTYPE html>
<html lang="en">
<head>
<meta charset="utf-8">
<title>Quorvant – Book Marketing Simplified</title>
<link href="https://fonts.googleapis.com/css2?family=Source+Sans+3:ital,wght@0,400;0,600;0,700;1,400&display=swap" rel="stylesheet">
<style>
:root{
  --brand:#1d4f8c;
  --brand-dark:#1f4d80;
  --nav:#22588f;
  --hero-a:#2e6aa8;
  --hero-b:#4f8fcb;
  --cta-a:#5cc0db;
  --cta-b:#3aa3c6;
  --cta-text:#1d5a7a;
  --text:#555b63;
  --green:#5a9b2a;
  --panel:#f0f0f0;
  --line:#d6d6d6;
  --white:#fff;
}
*{box-sizing:border-box;margin:0;padding:0}
html,body{width:1200px;height:935px;overflow:hidden;background:var(--white)}
body{position:relative;font-family:"Source Sans 3",Arial,sans-serif;color:var(--text)}
.abs{position:absolute}

.brand{left:181px;top:50px}
.brand-name{font-size:26px;line-height:30px;font-weight:600;color:var(--brand)}
.brand-tagline{margin-top:2px;font-size:12px;color:var(--text)}

.search{left:814px;top:57px;width:206px;height:20px;border:1px solid #c9c9c9;border-radius:3px;font-size:8px;color:#666;padding:5px 10px}
.search svg{position:absolute;right:8px;top:4px}

.nav{left:181px;top:109px;width:840px;height:33px;background:var(--nav);border-radius:3px 3px 0 0;display:flex;justify-content:space-around;align-items:center;font-size:10.5px;color:var(--white)}

.hero{left:181px;top:142px;width:840px;height:327px;background:linear-gradient(135deg,var(--hero-a),var(--hero-b));overflow:hidden}
.hero-map{position:absolute;left:230px;top:20px;width:470px;height:290px;background:radial-gradient(ellipse at center,rgba(255,255,255,.13),rgba(255,255,255,0) 70%)}
.hero-photo{position:absolute;left:543px;top:12px;width:262px;height:315px;background:linear-gradient(180deg,rgba(240,230,220,.35),rgba(255,255,255,.55));border-radius:120px 120px 0 0}
.hero h1{position:absolute;left:56px;top:90px;font-size:33px;line-height:34px;font-weight:600;color:var(--white)}
.hero h2{position:absolute;left:57px;top:132px;width:510px;font-size:13px;line-height:23px;font-weight:600;color:var(--white)}
.hero p{position:absolute;left:58px;top:184px;width:480px;font-size:10.2px;line-height:17px;color:var(--white)}
.hero .cta{position:absolute;left:59px;top:221px;width:225px;height:42px;background:linear-gradient(var(--cta-a),var(--cta-b));border-radius:3px;font-size:15px;color:var(--cta-text);display:flex;align-items:center;justify-content:center}
.dots{position:absolute;left:22px;top:302px;display:flex;gap:3px}
.dots span{width:9px;height:9px;background:#6f9ccc}
.dots span:first-child{background:#46b2d8}

.section-title{font-size:12.5px;font-weight:700;color:var(--brand)}
.welcome-title{left:181px;top:485px}
.welcome-photo{left:181px;top:517px;width:186px;height:87px;background:linear-gradient(90deg,#e9e4df,#c9c3bd 50%,#3b3d44)}
.welcome-text{left:392px;top:515px;width:305px;font-size:9.3px;line-height:15.5px}
.welcome-text p+p{margin-top:15.5px}
.welcome-more{left:181px;top:619px;width:520px;font-size:9.3px;line-height:15.5px}

.testi-title{left:721px;top:485px}
.testi-arrows{left:999px;top:489px;display:flex;gap:2px}
.testi-arrows span{width:9px;height:9px;background:#3e73ad;border-radius:1px}
.quote{left:722px;top:514px;width:298px;height:86px;border:1px solid var(--line);border-radius:3px;box-shadow:0 1px 3px rgba(0,0,0,.08)}
.quote p{position:absolute;left:34px;top:22px;width:250px;font-size:8.8px;line-height:15.5px;font-style:italic;color:#555}
.quote .qo,.quote .qc{position:absolute;font-size:22px;color:#c8c8c8;font-family:Georgia,serif}
.quote .qo{left:15px;top:2px}.quote .qc{right:14px;top:52px}
.quote-tail{left:800px;top:599px}
.avatar{left:722px;top:621px;width:51px;height:46px;border:1px solid var(--line);padding:2px}
.avatar div{width:100%;height:100%;background:linear-gradient(#c9d7e4,#8a9fb3)}
.author{left:782px;top:626px;font-size:9px;font-weight:700;color:var(--brand)}
.author-url{left:782px;top:643px;font-size:8.8px;font-style:italic;color:#555}

.doyou{left:181px;top:691px;width:522px;height:139px;background:var(--brand-dark);border-radius:3px;color:var(--white);padding:15px 20px}
.doyou h3{font-size:13px;font-weight:600}
.doyou ul{list-style:none;margin-top:8px}
.doyou li{font-size:10.8px;line-height:21.5px;padding-left:18px;position:relative}
.doyou li::before{content:"»";position:absolute;left:0;top:0}

.newsletter{left:722px;top:691px;width:298px;height:139px;background:linear-gradient(var(--panel),#fafafa);border-radius:3px;text-align:center}
.newsletter .kicker{margin-top:16px;font-size:12.5px;font-weight:600;color:var(--green)}
.newsletter .big{font-size:19px;font-weight:600;color:var(--brand);line-height:22px}
.newsletter .sub{margin-top:5px;font-size:10.5px;line-height:18px;color:#666}
.email{position:absolute;left:18px;top:102px;width:233px;height:22px;border:1px solid #d0d0d0;background:var(--white);font-size:8.5px;color:#999;padding:5px 10px;text-align:left}
.go{position:absolute;left:258px;top:102px;width:30px;height:21px;background:#5a5d62;border-radius:3px;color:var(--white);font-size:8.5px;display:flex;align-items:center;justify-content:center}

.footer{left:181px;top:852px;width:840px;height:83px;background:linear-gradient(#eeeeee,#fafafa)}
.footer-links{position:absolute;left:26px;top:21px;display:flex;font-size:8.8px;color:#555}
.footer-links span+span::before{content:"|";margin:0 13px;color:#777}
.copyright{position:absolute;left:26px;top:41px;font-size:8.8px;color:#555}
.connect{position:absolute;left:582px;top:33px;font-size:10.8px;font-weight:700;color:var(--brand)}
.social{position:absolute;left:706px;top:23px;display:flex;gap:2px}
.social span{width:27px;height:27px;border-radius:50%}
</style>
</head>
<body>
  <div class="abs brand">
    <div class="brand-name">Quorvant</div>
    <div class="brand-tagline">Book Marketing Simplified</div>
  </div>

  <div class="abs search">SEARCH :
    <svg width="12" height="12" viewBox="0 0 12 12"><circle cx="5" cy="5" r="3.5" fill="none" stroke="#999" stroke-width="1.3"/><line x1="7.5" y1="7.5" x2="11" y2="11" stroke="#999" stroke-width="1.8"/></svg>
  </div>

  <nav class="abs nav">
    <span>HOME</span><span>SERVICES</span><span>ABOUT US</span><span>RESOURCES</span><span>OUR CLIENTS</span><span>TESTIMONIALS</span><span>BLOG</span><span>CONTACT US</span>
  </nav>

  <section class="abs hero">
    <div class="hero-map" role="img" aria-label="Faint dotted world map in the background"></div>
    <div class="hero-photo" role="img" aria-label="Photo of a smiling man in a white shirt with arms crossed"></div>
    <h1>QUORVANT MARKETING</h1>
    <h2>IS BOOK MARKETING SERVICE THAT THAT PROVIDES AUTHORS WITH AN EFFECTIVE, AFFORDABLE APPROACH TO MARKETING THEIR BOOK.</h2>
    <p>We provide marketing coaching and consulting services that accelerate book sales, target your ideal reader and develop a community of fans that will promote your book for you.</p>
    <div class="cta">CLICK HERE FOR MORE INFO</div>
    <div class="dots"><span></span><span></span><span></span><span></span></div>
  </section>

  <h2 class="abs section-title welcome-title">WELCOME TO QUORVANT</h2>
  <div class="abs welcome-photo" role="img" aria-label="Photo of three smiling business people"></div>
  <div class="abs welcome-text">
    <p>QuorVant Marketing is a coaching service that provides small business owners an effective, affordable approach to marketing.</p>
    <p>Our objective is to help you learn the skills to market your business, find ideal clients, increase sales, and maintain the momentum you need to achieve your goals.</p>
  </div>
  <p class="abs welcome-more">Whether your business is a retail store, online start-up, home based business or health care practice, you can develop the skills to manage high impact, low cost marketing campaigns for your organization.</p>

  <h2 class="abs section-title testi-title">TESTIMONIALS</h2>
  <div class="abs testi-arrows"><span></span><span></span></div>
  <div class="abs quote">
    <span class="qo">“</span>
    <p>Since I started working with Miriam to develop my ‘author platform’, Chirply followers are up, retweets are up and January visits to my website are through the roof! She’s a magician!</p>
    <span class="qc">”</span>
  </div>
  <svg class="abs quote-tail" width="40" height="22" viewBox="0 0 40 22"><path d="M0 0 L5 21 L40 0" fill="#fff" stroke="#d6d6d6"/><line x1="1" y1="0.5" x2="39" y2="0.5" stroke="#fff" stroke-width="2"/></svg>
  <div class="abs avatar"><div role="img" aria-label="Portrait photo of the reviewer"></div></div>
  <div class="abs author">DANA PREWITT</div>
  <div class="abs author-url">www.harborleafhomes.com</div>

  <section class="abs doyou">
    <h3>DO YOU</h3>
    <ul>
      <li>Want to be a best selling author, but need someone to show you the way</li>
      <li>Wonder what is the secret to achieving high book sales?</li>
      <li>Worry that you aren’t doing the right things to ensure that your book is a success?</li>
      <li>Need someone to help keep your spirits up and maintain momentum?</li>
    </ul>
  </section>

  <section class="abs newsletter">
    <div class="kicker">SIGN UP FOR</div>
    <div class="big">OUR FREE NEWSLETTER</div>
    <div class="sub">and receive our list of Top Chirply<br>Tips for Authors Free!</div>
    <div class="email">Enter email address</div>
    <div class="go">GO</div>
  </section>

  <footer class="abs footer">
    <div class="footer-links"><span>Home</span><span>Services</span><span>About Us</span><span>Resources</span><span>Our clients</span><span>Testimonials</span><span>Blog</span><span>Contact Us</span></div>
    <div class="copyright">Copyrights © 2013. Quorvant. All rights reserved.</div>
    <div class="connect">CONNECT WITH MIRIAM</div>
    <div class="social">
      <span style="background:#2f63a8" role="img" aria-label="Facemuro"></span>
      <span style="background:#3aa6d6" role="img" aria-label="Chirply"></span>
      <span style="background:#2a79a8" role="img" aria-label="Pindle up"></span>
      <span style="background:#3a3a3a" role="img" aria-label="Vexor+"></span>
    </div>
  </footer>
</body>
</html>
```